Christmas and New Year wishes

I would like to send as a picture in a email a graphic that relates to:
-thanks for the collaboration / partnership in the past year (to be used for customers and partners)
-Wishes for Merry christmas and a successful 2019
-it should be colored and possibly include our logo color (www.velkari.ch) (nice to have), or the name of our company

Target Market(s)

Customers and partners

Industry/Entity Type

It Company

Font styles to use
Sans Serif

Colors
9bcb3c
0455a3

Requirements
Must have
• Relation to christmas
• Relation to New year
Nice to have
• The colors below are near to the company logo color. But feel free to use any other logo
• a funny design
• Happy Customer or partner (supplier)
• Can be a mixture of text and drawing

```html
<!DOCTYPE html>
<html lang="en">
<head>
<meta charset="utf-8">
<title>Velkari – Season's Greetings 2019</title>
<link href="https://fonts.googleapis.com/css2?family=Kaushan+Script&family=Montserrat:wght@300;600&display=swap" rel="stylesheet">
<style>
  :root {
    --board: #b9b5b3;
    --green-in: #3ab54a;
    --green-out: #009245;
    --blue-in: #29abe2;
    --blue-out: #0068b5;
    --red-in: #ff0000;
    --red-out: #c1272d;
    --lime-in: #d7e232;
    --lime-out: #8aa915;
    --ink-orange: #f7531d;
    --ink-dark: #111111;
    --white: #ffffff;
    --forest-lime: #cfd535;
    --forest-slate: #5a7d8e;
    --brand-slate: #4f7386;
    --note: #2f4a4a;
  }
  * { box-sizing: border-box; margin: 0; padding: 0; }
  html, body { width: 1180px; height: 1200px; overflow: hidden; }
  body { background: var(--board); position: relative; }

  .card {
    position: absolute;
    width: 520px;
    height: 527px;
    background: var(--white);
    overflow: hidden;
    box-shadow: 0 6px 24px rgba(0,0,0,0.25);
  }
  .card--green { left: 34px;  top: 30px;  }
  .card--blue  { left: 624px; top: 30px;  }
  .card--red   { left: 32px;  top: 596px; }
  .card--lime  { left: 622px; top: 596px; }

  .sky { position: absolute; left: 0; top: 0; width: 100%; height: 330px; }
  .card--green .sky { background: radial-gradient(circle at 50% 80%, var(--green-in), var(--green-out) 70%); }
  .card--blue  .sky { background: radial-gradient(circle at 50% 80%, var(--blue-in), var(--blue-out) 70%); }
  .card--red   .sky { background: radial-gradient(circle at 50% 80%, var(--red-in), var(--red-out) 70%); }
  .card--lime  .sky { background: radial-gradient(circle at 50% 80%, var(--lime-in), var(--lime-out) 70%); }

  .forest {
    position: absolute; left: 0; top: 290px; width: 100%; height: 130px;
  }
  .card--green .forest, .card--blue .forest { background: linear-gradient(to bottom, var(--forest-lime) 0%, var(--forest-lime) 45%, var(--white) 100%); }
  .card--red .forest, .card--lime .forest { background: linear-gradient(to bottom, var(--forest-slate) 0%, var(--forest-slate) 45%, var(--white) 100%); }

  .greeting {
    position: absolute; left: 0; width: 100%; text-align: center;
    font-family: "Kaushan Script", cursive; line-height: 1;
  }
  .greeting__merry { top: 58px; font-size: 66px; color: var(--ink-orange); }
  .card--red .greeting__merry { color: var(--white); }
  .greeting__wish { top: 128px; font-size: 60px; color: var(--ink-dark); }
  .greeting__year { top: 188px; font-size: 72px; color: var(--white); }

  .brand {
    position: absolute; left: 0; top: 436px; width: 100%; text-align: center;
    font-family: "Montserrat", sans-serif; font-weight: 300;
    font-size: 38px; letter-spacing: 2px; color: var(--brand-slate);
  }
  .thanks {
    position: absolute; left: 0; top: 480px; width: 100%; text-align: center;
    font-family: "Montserrat", sans-serif; font-weight: 600;
    font-size: 12px; line-height: 12px; color: var(--note);
    font-variant: small-caps; letter-spacing: 0.5px;
  }
</style>
</head>
<body>

<section class="card card--green">
  <div class="sky"></div>
  <div class="forest" role="img" aria-label="Silhouette of snowy pine forest in lime and white"></div>
  <p class="greeting greeting__merry">Merry Christmas</p>
  <p class="greeting greeting__wish">and a successful</p>
  <p class="greeting greeting__year">2019</p>
  <p class="brand">VELKARI</p>
  <p class="thanks">Thank you for your collaboration<br>and partnership in the past year</p>
</section>

<section class="card card--blue">
  <div class="sky"></div>
  <div class="forest" role="img" aria-label="Silhouette of snowy pine forest in lime and white"></div>
  <p class="greeting greeting__merry">Merry Christmas</p>
  <p class="greeting greeting__wish">and a successful</p>
  <p class="greeting greeting__year">2019</p>
  <p class="brand">VELKARI</p>
  <p class="thanks">Thank you for your collaboration<br>and partnership in the past year</p>
</section>

<section class="card card--red">
  <div class="sky"></div>
  <div class="forest" role="img" aria-label="Silhouette of snowy pine forest in slate blue and white"></div>
  <p class="greeting greeting__merry">Merry Christmas</p>
  <p class="greeting greeting__wish">and a successful</p>
  <p class="greeting greeting__year">2019</p>
  <p class="brand">VELKARI</p>
  <p class="thanks">Thank you for your collaboration<br>and partnership in the past year</p>
</section>

<section class="card card--lime">
  <div class="sky"></div>
  <div class="forest" role="img" aria-label="Silhouette of snowy pine forest in slate blue and white"></div>
  <p class="greeting greeting__merry">Merry Christmas</p>
  <p class="greeting greeting__wish">and a successful</p>
  <p class="greeting greeting__year">2019</p>
  <p class="brand">VELKARI</p>
  <p class="thanks">Thank you for your collaboration<br>and partnership in the past year</p>
</section>

</body>
</html>
```